K&M Trailer Rental promo Flyer 5.5x8.5" Flyer

All assets and several pictures of my trailers, that we rent out, are attached.

Flyer dimensions are 5.5"x8.5" - I'll be having it printed on glossy stock.
The dimensions and capacity of the trailers is key.
Include phone number: 248-555-0186 and our website kandmtrailer-example.com

I want something that will really "POP".

Target Market(s)

Blue collar business owners. Recreational offer roads/4x4 folks, used car dealers, contractors/small business owners. Folks with only occasional need for a trailer

Industry/Entity Type

Trailer Rental

Font styles to use
Other font styles liked:
• Designer's choice/no preference

Colors
EE7325
F08F49
F5BC92
FAE3D3
FDF4ED

Requirements
Must have
• Phone number, website, and details about our trailer offerings

```html
<!DOCTYPE html>
<html lang="en">
<head>
<meta charset="UTF-8">
<title>K&amp;M Trailer Rental Flyer</title>
<link rel="stylesheet" href="https://fonts.googleapis.com/css2?family=Bebas+Neue&family=Poppins:wght@500;600;700&display=swap">
<style>
  :root {
    --orange-deep: #EE7325;
    --orange: #F08F49;
    --peach: #F5BC92;
    --cream: #FAE3D3;
    --paper: #FFFFFF;
    --ink: #1E1E1E;
    --white: #FFFFFF;
  }
  * { margin: 0; padding: 0; box-sizing: border-box; }
  html, body { width: 850px; height: 1200px; overflow: hidden; background: #F4F4F4; }
  .flyer {
    position: absolute; left: 37px; top: 0;
    width: 776px; height: 1200px;
    background: var(--paper);
    font-family: "Poppins", sans-serif;
    overflow: hidden;
  }
  .abs { position: absolute; }
  .display { font-family: "Bebas Neue", sans-serif; font-weight: 400; }

  .brand-box {
    left: 209px; top: 0; width: 358px; height: 113px;
    background: var(--peach);
    display: flex; align-items: flex-end; justify-content: center;
    padding-bottom: 12px;
  }
  .brand-name { font-family: "Bebas Neue", sans-serif; font-size: 34px; color: var(--ink); letter-spacing: 0.5px; }

  .accent-bar { background: var(--peach); }
  .accent-top-left { left: 0; top: 130px; width: 77px; height: 13px; }
  .accent-top-right { left: 703px; top: 130px; width: 74px; height: 13px; }

  .hero-photo {
    left: 0; top: 143px; width: 776px; height: 303px;
    background: linear-gradient(90deg, #8F969B 0%, #C9CCCC 30%, #BDB9B0 55%, #9AA38B 80%, #C2C4C4 100%);
  }
  .hero-tint {
    left: 209px; top: 143px; width: 358px; height: 303px;
    background: rgba(238, 115, 37, 0.72);
  }
  .hero-title {
    left: 209px; top: 390px; width: 358px; text-align: center;
    font-size: 46px; color: var(--white); letter-spacing: 0.5px; line-height: 1;
  }

  .offer-bar-left { left: 0; top: 470px; width: 75px; height: 30px; }
  .offer-bar-right { left: 702px; top: 470px; width: 75px; height: 30px; }
  .offer-heading {
    left: 75px; top: 464px; width: 627px; text-align: center;
    font-size: 40px; font-style: italic; color: var(--ink); line-height: 1.05;
  }

  .trailer-row { left: 0; width: 776px; height: 198px; }
  .row-one { top: 535px; background: var(--orange); }
  .row-two { top: 750px; background: var(--peach); }

  .trailer-photo {
    left: 24px; top: 20px; width: 297px; height: 162px;
    border: 4px solid var(--white);
  }
  .row-one .trailer-photo { background: linear-gradient(160deg, #5A5D60 0%, #3A3C3F 55%, #8E9094 100%); }
  .row-two .trailer-photo { background: linear-gradient(160deg, #9A9C9E 0%, #7B7D80 50%, #B5A27A 100%); }
  .trailer-tag {
    position: absolute; left: 0; bottom: 0; height: 26px; padding: 0 24px 0 12px;
    background: var(--orange-deep); color: var(--white);
    font-size: 12px; font-weight: 700; line-height: 26px; white-space: nowrap;
    clip-path: polygon(0 0, 100% 0, 92% 100%, 0 100%);
  }
  .rate-strip {
    left: 321px; top: 42px; width: 441px; height: 36px;
    background: var(--white);
    clip-path: polygon(0 0, 100% 0, 96% 100%, 0 100%);
  }
  .rate-head { top: 47px; font-size: 18px; font-weight: 700; color: var(--orange-deep); line-height: 26px; }
  .rate-col-week { left: 344px; }
  .rate-col-weekend { left: 571px; }
  .rate-body { top: 94px; font-size: 19px; font-weight: 600; color: var(--white); line-height: 27.5px; }
  .rate-col-weekend.rate-body { top: 96px; }

  .service-box {
    left: 27px; top: 990px; width: 408px; height: 163px;
    border: 3px solid var(--ink);
  }
  .pin-icon { left: 52px; top: 970px; width: 76px; height: 96px; background: var(--paper); padding: 0 6px; }
  .service-title { left: 144px; top: 1022px; font-size: 44px; color: var(--ink); line-height: 1; }
  .service-city { font-size: 14px; font-weight: 600; color: var(--orange); line-height: 21.5px; }
  .city-col-1 { left: 49px; top: 1076px; }
  .city-col-2 { left: 162px; top: 1076px; }
  .city-col-3 { left: 277px; top: 1076px; }

  .phone-band { left: 457px; top: 1062px; width: 320px; height: 84px; background: var(--orange); }
  .phone-icon { left: 462px; top: 993px; width: 93px; height: 89px; }
  .phone-number {
    left: 457px; top: 1076px; width: 320px; padding-left: 7px;
    font-size: 37px; font-weight: 700; color: var(--white); line-height: 1; letter-spacing: 0.5px;
  }
  .website {
    left: 457px; top: 1117px; width: 320px; padding-left: 9px;
    font-size: 15px; font-weight: 600; color: var(--white); line-height: 20px;
  }
</style>
</head>
<body>
<main class="flyer">
  <header class="abs brand-box">
    <span class="brand-name">K&amp;M Trailer Rental</span>
  </header>

  <div class="abs accent-bar accent-top-left"></div>
  <div class="abs accent-bar accent-top-right"></div>

  <div class="abs hero-photo" role="img" aria-label="Photo of a vintage motorhome loaded on a black flatbed car hauler hitched to a pickup truck"></div>
  <div class="abs hero-tint"></div>
  <h1 class="abs hero-title display">K&amp;M Trailer Rental</h1>

  <div class="abs accent-bar offer-bar-left"></div>
  <div class="abs accent-bar offer-bar-right"></div>
  <h2 class="abs offer-heading display">Trailers we have available to offer you</h2>

  <section class="abs trailer-row row-one">
    <div class="abs trailer-photo" role="img" aria-label="Photo of a black 20 foot car hauler trailer with a wooden deck in a parking lot">
      <span class="trailer-tag">RX 20' X 7' CAR HAULER · 7,000 LB</span>
    </div>
    <div class="abs rate-strip"></div>
    <h3 class="abs rate-head rate-col-week">WEEK RATES</h3>
    <h3 class="abs rate-head rate-col-weekend">WEEKEND RATES</h3>
    <p class="abs rate-body rate-col-week">Monday to Thursday<br>$85/Day*<br>$350/Week*</p>
    <p class="abs rate-body rate-col-weekend">Friday to Sunday<br>$85/Day*<br>$200/Weekend*</p>
  </section>

  <section class="abs trailer-row row-two">
    <div class="abs trailer-photo" role="img" aria-label="Photo of a black tilt car hauler trailer with a wooden deck on asphalt">
      <span class="trailer-tag">RX 20' X 7' CAR HAULER · 7,000 LB</span>
    </div>
    <div class="abs rate-strip"></div>
    <h3 class="abs rate-head rate-col-week">WEEK RATES</h3>
    <h3 class="abs rate-head rate-col-weekend">WEEKEND RATES</h3>
    <p class="abs rate-body rate-col-week">Monday to Thursday<br>$85/Day*<br>$350/Week*</p>
    <p class="abs rate-body rate-col-weekend">Friday to Sunday<br>$85/Day*<br>$200/Weekend*</p>
  </section>

  <div class="abs service-box"></div>
  <svg class="abs pin-icon" viewBox="0 0 64 96" aria-hidden="true">
    <ellipse cx="32" cy="86" rx="28" ry="8" fill="#F08F49"/>
    <path d="M32 4 C16 4 5 15 5 30 C5 48 32 78 32 78 C32 78 59 48 59 30 C59 15 48 4 32 4 Z" fill="#F08F49"/>
    <circle cx="32" cy="29" r="10" fill="#FFFFFF"/>
  </svg>
  <h2 class="abs service-title display">Area of Service</h2>
  <p class="abs service-city city-col-1">WAYNE. MI<br>GENESEE. MI<br>MONROE. MI</p>
  <p class="abs service-city city-col-2">LAPEER. MI<br>ST. CLAIR. MI</p>
  <p class="abs service-city city-col-3">WASHTENAW. MI<br>LIVINGSTON. MI</p>

  <div class="abs phone-band"></div>
  <svg class="abs phone-icon" viewBox="0 0 93 89" aria-hidden="true">
    <rect x="2" y="2" width="89" height="85" rx="12" fill="#F08F49"/>
    <rect x="10" y="10" width="73" height="69" rx="6" fill="#FFFFFF"/>
    <path d="M30 20 L38 19 L44 33 L38 38 C41 46 47 52 55 56 L60 50 L74 56 L73 64 C72 68 68 70 64 70 C42 68 25 51 23 29 C23 24 26 21 30 20 Z" fill="#F08F49"/>
  </svg>
  <p class="abs phone-number">(248)555-0186</p>
  <p class="abs website">kandmtrailer-example.com</p>
</main>
</body>
</html>
```